Zielgruppe
Wir sind ein IT Systemhaus mit einem Scherpunkt auf Wireless LAN für Gewerbekunden
https://www.quarvelo-netz.de/wlan-beratung/
Aufgabenstellung
Im Anhang finden Sie einige Stichpunkte/Texte und eine PPT mit Grafiken, sowie unser Briefpapier.
Ziel ist es 1 Flyer A4 Einseitig zu erhalten – Wir benötigen diesen As soon as possible
Das Thema lautet hier:
1. Lernoffensive Klassen
Grafiken können Sie aus der PPT oder der Webseite entnehmen
Die Flyer sollten im oberen Bereich wie unser Briefpapier aussehen und Farbmäßig unserem CD entsprechen
#1e73be
Den Orangeton finde ich leider gerade nicht ☹
An Ergänzenden Grafiken sind wir ebenfalls Interessiert.
Die Welle haben wir leider nicht als Vectorgrafik

```html
<!DOCTYPE html>
<html lang="de">
<head>
<meta charset="utf-8">
<title>Lernoffensive Klassen Rheinland-Pfalz – Quarvelo</title>
<link href="https://fonts.googleapis.com/css2?family=Open+Sans:ital,wght@0,300;0,400;1,300;1,400;1,600&display=swap" rel="stylesheet">
<style>
  :root {
    --brand-blue: #1e73be;
    --wave-mid: #3a9ad9;
    --wave-light: #a9d3ef;
    --wave-pale: #d6ebf8;
    --text-grey: #555a5f;
    --copy-grey: #6b7075;
    --logo-grey: #56595c;
    --paper: #ffffff;
    --photo-warm: #d9c7b2;
    --photo-cool: #5f88b8;
  }
  * { box-sizing: border-box; margin: 0; padding: 0; }
  html, body { width: 880px; height: 1200px; overflow: hidden; background: var(--paper); }
  body { font-family: "Open Sans", Arial, sans-serif; color: var(--text-grey); }
  .flyer { position: relative; width: 880px; height: 1200px; overflow: hidden; background: var(--paper); }

  .header-wave, .footer-wave { position: absolute; left: 0; width: 880px; }
  .header-wave { top: 0; height: 160px; }
  .footer-wave { bottom: 0; height: 130px; z-index: 3; }

  .brand { position: absolute; top: 80px; right: 48px; }
  .brand-name { font-weight: 300; font-size: 42px; letter-spacing: 5px; color: var(--logo-grey); line-height: 1; }

  .title { position: absolute; top: 180px; left: 34px; font-style: italic; font-weight: 400; font-size: 37px; color: var(--brand-blue); letter-spacing: 0.2px; }

  .benefits { position: absolute; top: 252px; left: 36px; width: 450px; }
  .benefit-group + .benefit-group { margin-top: 45px; }
  .benefit-group h2 { font-style: italic; font-weight: 400; font-size: 16.5px; line-height: 25px; color: var(--text-grey); margin-bottom: 10px; }
  .benefit-group ul { list-style: none; }
  .benefit-group li { font-style: italic; font-weight: 300; font-size: 16.5px; line-height: 25px; padding-left: 26px; position: relative; color: var(--text-grey); }
  .benefit-group li::before { content: "•"; position: absolute; left: 4px; }

  .intro { position: absolute; top: 254px; left: 489px; width: 364px; font-style: italic; font-weight: 300; font-size: 14.2px; line-height: 25px; color: var(--copy-grey); }
  .intro p + p { margin-top: 25px; }

  .photo { position: absolute; left: 380px; top: 672px; width: 500px; height: 528px; z-index: 1; }

  .advantages { position: absolute; left: 31px; top: 750px; width: 358px; height: 424px; background: var(--brand-blue); z-index: 4; padding: 26px 22px 0 22px; color: var(--paper); }
  .advantages h2 { font-style: italic; font-weight: 600; font-size: 18px; margin-bottom: 14px; }
  .advantages ul { list-style: none; }
  .advantages li { font-style: italic; font-weight: 400; font-size: 14.5px; line-height: 21px; padding-left: 16px; position: relative; margin-bottom: 21px; }
  .advantages li::before { content: "•"; position: absolute; left: 0; }

  .web { position: absolute; right: 32px; bottom: 22px; z-index: 5; font-style: italic; font-weight: 600; font-size: 16px; color: var(--paper); }
</style>
</head>
<body>
<main class="flyer">
  <svg class="header-wave" viewBox="0 0 880 160" preserveAspectRatio="none" aria-hidden="true">
    <path d="M0 0 H880 V12 C700 10 560 40 420 78 C280 116 120 150 0 150 Z" fill="var(--wave-pale)"/>
    <path d="M0 0 H880 V8 C680 12 520 30 380 58 C240 86 110 118 0 124 Z" fill="var(--wave-light)"/>
    <path d="M0 0 H760 C600 10 460 30 330 50 C200 70 90 92 0 96 Z" fill="var(--wave-mid)"/>
    <path d="M0 0 H600 C470 6 350 22 240 40 C150 55 70 66 0 70 Z" fill="var(--brand-blue)"/>
  </svg>

  <div class="brand">
    <span class="brand-name">QUARVELO</span>
  </div>

  <h1 class="title">Lernoffensive Klassen Rheinland-Pfalz</h1>

  <section class="benefits">
    <div class="benefit-group">
      <h2>Mehrwert für die Schule:</h2>
      <ul>
        <li>90% der Kosten werden vom Staat übernommen</li>
        <li>Reputationsvorteil durch digitales Lernangebot</li>
        <li>Moderne Unterrichtsmethoden</li>
      </ul>
    </div>
    <div class="benefit-group">
      <h2>Mehrwert für die Schüler:</h2>
      <ul>
        <li>routinierter Umgang mit modernen Medien</li>
        <li>Verbesserte Lernerfolge</li>
        <li>Zeitgemäße Medienkompetenzen</li>
      </ul>
    </div>
    <div class="benefit-group">
      <h2>Die Quarvelo GmbH bietet:</h2>
      <ul>
        <li>Unterstützung während der Antragsstellung</li>
        <li>Erfahrung mit Schulen</li>
        <li>Professionelle WLAN-Beratung von<br>Konzept bis zur Konfiguration</li>
      </ul>
    </div>
  </section>

  <section class="intro">
    <p>WLAN in der Schule einrichten? Selbstverständlich verstehen wir, dass dies auf den ersten Blick problematisch erscheint, da es vermutlich Schüler gibt, die versuchen würden, das Angebot auszunutzen. Allerdings gehört zu unserem erstklassigen Service dazu, dass Sie als Verantwortlicher ganz genau festlegen können, wer in welchem Bereich und zu welcher Zeit Zugang zum schuleigenen WLAN haben soll.</p>
    <p>Dadurch kann man beispielsweise Oberstufenschülern in Freistunden mehr Flexibilität anbieten, die Hausaufgabenbetreuung in den Nachmittagsstunden bereichern oder die Recherche im Rahmen des Unterrichts vereinfachen. Verschließen Sie sich nicht vor modernen Medien, sondern nutzen Sie die Vorteile einer funktionierenden IT-Infrastruktur für die Unterrichtsgestaltung.</p>
  </section>

  <svg class="photo" viewBox="0 0 500 528" preserveAspectRatio="none" role="img" aria-label="Foto: lächelnder Schüler im blauen Polohemd arbeitet im Klassenzimmer an einem Tablet">
    <defs>
      <linearGradient id="photoTone" x1="0" y1="0" x2="1" y2="1">
        <stop offset="0" stop-color="var(--photo-warm)"/>
        <stop offset="0.4" stop-color="#c9b8a4"/>
        <stop offset="0.8" stop-color="var(--photo-cool)"/>
        <stop offset="1" stop-color="#36476a"/>
      </linearGradient>
    </defs>
    <path d="M0 88 C150 72 340 34 500 10 V528 H0 Z" fill="url(#photoTone)"/>
  </svg>

  <section class="advantages">
    <h2>Ihre Vorteile auf einen Blick:</h2>
    <ul>
      <li>Integration von modernen Lernmethoden</li>
      <li>ständig verfügbare, digitale<br>Lernumgebungen</li>
      <li>digitale Kommunikationswege<br>zwischen Lehrern und Schülern</li>
      <li>direktes Feedback für Schüler<br>und Lehrer</li>
      <li>Einbindung von BYOD-Konzepten<br>und Screencasting</li>
      <li>Remote-Zugriff auf den Unterricht<br>von Zuhause</li>
    </ul>
  </section>

  <svg class="footer-wave" viewBox="0 0 880 130" preserveAspectRatio="none" aria-hidden="true">
    <path d="M0 70 C200 40 420 60 620 30 C720 15 810 8 880 10 V130 H0 Z" fill="var(--wave-pale)"/>
    <path d="M0 95 C220 70 440 85 640 55 C740 40 820 34 880 34 V130 H0 Z" fill="var(--wave-light)"/>
    <path d="M0 112 C240 96 460 104 660 80 C760 68 830 62 880 60 V130 H0 Z" fill="var(--wave-mid)"/>
    <path d="M0 124 C260 116 480 118 680 100 C780 92 840 88 880 86 V130 H0 Z" fill="var(--brand-blue)"/>
  </svg>
  <div class="web">www.quarvelo-netz.de</div>
</main>
</body>
</html>
```